Private Dining Restaurant Menu Design

Looking for help in designing a private dining room menu brochure - probably would need 4 panel layout to make all of the content fit, or a 5.5x8" booklet. Open to your ideas on layout/vessel - would want to post on website and be able to print to hand out to guests interested in booking our private dining room.

All content is in the attached "Private Dining Menu".

Would like to match existing dinner menu design - also attached.

Website is www.tallowfenkitchen.com

Requirements
Must have
• Easy to read format of a brochure of the private dining menu content - want to be able to hand out to interested guests and have it simple and easy to read/flip through.

```html
<!DOCTYPE html>
<html lang="en">
<head>
<meta charset="utf-8">
<title>Dinner Options – Private Dining</title>
<link href="https://fonts.googleapis.com/css2?family=Oswald:wght@500;600&family=Open+Sans:ital,wght@0,400;0,600;0,700;1,400&display=swap" rel="stylesheet">
<style>
  :root {
    --paper: #fbfaf8;
    --paper-wash: #efece8;
    --accent: #d35a2c;
    --ink: #3a3836;
    --muted: #6d6a67;
    --rule: #c9b9b0;
    --photo-dark: #4a3f36;
    --photo-mid: #8c7a68;
    --photo-light: #d9cfc3;
  }
  * { margin: 0; padding: 0; box-sizing: border-box; }
  html, body { width: 826px; height: 1200px; overflow: hidden; }
  body {
    background: radial-gradient(ellipse at 50% 45%, var(--paper) 55%, var(--paper-wash) 100%);
    font-family: "Open Sans", Arial, sans-serif;
    color: var(--ink);
    position: relative;
  }
  .menu-page { position: absolute; left: 62px; top: 38px; width: 710px; }
  .page-title {
    font-family: "Oswald", "Arial Narrow", sans-serif;
    font-weight: 600; font-size: 36px; line-height: 1;
    color: var(--accent); letter-spacing: 0.5px;
  }
  .page-subtitle {
    font-family: "Oswald", "Arial Narrow", sans-serif;
    font-weight: 500; font-size: 20px; color: var(--accent);
    margin-top: 6px; letter-spacing: 0.2px;
  }
  .page-note {
    font-style: italic; font-size: 14.5px; color: var(--muted);
    line-height: 1.45; margin-top: 14px; width: 690px;
  }
  .divider { border: 0; border-top: 1.5px solid var(--rule); margin: 18px 0 20px; }
  .option-title {
    font-family: "Oswald", "Arial Narrow", sans-serif;
    font-weight: 600; font-size: 24px; color: var(--accent); letter-spacing: 0.3px;
  }
  .option-desc {
    font-weight: 700; font-size: 15px; line-height: 1.5;
    color: var(--ink); margin-top: 8px; width: 690px;
  }
  .option-items { list-style: none; margin-top: 18px; }
  .option-items li {
    font-size: 15px; line-height: 1.75; color: var(--muted);
  }
  .option-items li::before { content: "- "; }
  .room-photo {
    position: absolute; left: 143px; top: 707px; width: 467px; height: 380px;
    background: linear-gradient(170deg, var(--photo-light) 0%, var(--photo-mid) 45%, var(--photo-dark) 100%);
  }
</style>
</head>
<body>
  <main class="menu-page">
    <h1 class="page-title">DINNER OPTIONS</h1>
    <p class="page-subtitle">(an option below must be chosen for groups of 15 or more, served after 3pm)</p>
    <p class="page-note">*It is greatly appreciated if you are able to give pre-determined individual menu orders to help with food prep and operations of the event</p>
    <hr class="divider">

    <section class="option">
      <h2 class="option-title">OPTION A - $20/PERSON</h2>
      <p class="option-desc">Served with bacon &amp; scallion mashed potatoes and steamed broccoli Also includes choice of starter house or Caesar salad</p>
      <ul class="option-items">
        <li>½ Tallowfen's Famous Wood-Roasted Chicken</li>
        <li>½ Slab Sweet &amp; Smoky BBQ Baby Back Ribs</li>
        <li>6 oz Fresh Norwegian Salmon</li>
        <li>6 oz Wood-Grilled Sirloin</li>
      </ul>
    </section>
    <hr class="divider">

    <section class="option">
      <h2 class="option-title">OPTION B - $27/PERSON</h2>
      <p class="option-desc">Served with bacon &amp; scallion mashed potatoes and steamed broccoli Also includes choice of starter house or Caesar salad</p>
      <ul class="option-items">
        <li>30-Day Aged Wood-Grilled Ribeye – 14 oz</li>
        <li>6 oz Wood-Grilled Sirloin &amp; Grilled Shrimp</li>
        <li>½ Slab BBQ Ribs &amp; ¼ Wood-Roasted Chicken</li>
        <li>Full Rack of BBQ Baby Back Ribs</li>
      </ul>
    </section>
    <hr class="divider" style="margin-top:62px">
  </main>

  <div class="room-photo" role="img" aria-label="Private dining room set with round tables, dark napkins and chandeliers beside tall windows and a stone fireplace"></div>
</body>
</html>
```